Circular Wedding Menu Design - Adobe Illustrator

I am looking for a design for circular wedding menus. these will be 7 inches.I'm providing a template from the printer, AI files of our wedding invitation, and the menu items.

The paper our invitations were printed on was a sandy beige color. please make the background for this the same color. It will be put ontop of a white plate with ivory tablecloth and cappucino covered napkins.

IMPORTANT - We aren't committed to a specific design so feel free to use whatever you like, but we definitely want the cow, fish, and carrot images from our rsvp to be used for the entrees in the menu.

IMPORTANT - must be in Adobe illustrator format

for inspiration:
http://cdn.plumbridalpages.example/wp-content/uploads/2012/10/harvel-styled-19.jpg

http://www.pictofind.example/imgres?imgurl=http%3A%2F%2Fwww.velvetknotstudio.example%2Fblog%2Fwp-content%2Fuploads%2F2013%2F07%2FRound-Menu-Wedding-Place-Setting.jpg&imgrefurl=http%3A%2F%2Fwww.velvetknotstudio.example%2Fblog%2Finspiration%2Fsimply-lovely-wedding-menu-place-settings%2F&h=815&w=600&zoom=1&page=1&start=0&ndsp=30

https://thumbs3.pictofind.example/images?q=tbn:Xk4mPq7RtL2vNw9HbYc3JdZs8FgQe1Ua

https://thumbs3.pictofind.example/images?q=tbn:Rb6wLn2TqZ8kVe4MhXs1PcYj9DuGa3Wo

https://thumbs2.pictofind.example/images?q=tbn:Hn5cWq8JtM3sLz7PxVb2KeRd6YgFo1Ni

```html
<!DOCTYPE html>
<html lang="en">
<head>
<meta charset="utf-8">
<title>Wedding Menu</title>
<link rel="stylesheet" href="https://fonts.googleapis.com/css2?family=Arvo:wght@700&family=Didact+Gothic&family=Fredericka+the+Great&display=swap">
<style>
  :root {
    --page: #ffffff;
    --sand: #e5e1d2;
    --gold: #b48c31;
    --ink: #1b1916;
    --rim: #2e2c29;
  }
  html, body {
    margin: 0;
    padding: 0;
    width: 1200px;
    height: 1156px;
    overflow: hidden;
    background: var(--page);
  }
  .menu-card {
    position: relative;
    width: 1200px;
    height: 1156px;
    overflow: hidden;
  }
  .card-disc {
    position: absolute;
    inset: 0;
  }
  .title-small {
    position: absolute;
    left: 0;
    width: 1142px;
    top: 34px;
    margin: 0;
    text-align: center;
    font-family: "Fredericka the Great", cursive;
    font-weight: 400;
    font-size: 58px;
    line-height: 1;
    color: var(--gold);
    letter-spacing: 2px;
  }
  .title-large {
    position: absolute;
    left: 0;
    width: 1142px;
    top: 72px;
    margin: 0;
    text-align: center;
    font-family: "Fredericka the Great", cursive;
    font-weight: 400;
    font-size: 196px;
    line-height: 1;
    color: var(--gold);
  }
  .ornament {
    position: absolute;
    background: var(--gold);
    opacity: 0.75;
  }
  .ornament--title-left { left: 395px; top: 73px; width: 108px; height: 6px; border-radius: 3px; }
  .ornament--title-right { left: 623px; top: 73px; width: 108px; height: 6px; border-radius: 3px; }
  .ornament--divider-one { left: 511px; top: 486px; width: 118px; height: 5px; border-radius: 3px; }
  .ornament--divider-two { left: 518px; top: 787px; width: 116px; height: 5px; border-radius: 3px; }
  .ornament--flourish {
    left: 265px; top: 954px; width: 615px; height: 80px;
    border-radius: 50%;
    background: radial-gradient(ellipse at center, rgba(180,140,49,0.55) 0%, rgba(180,140,49,0.25) 55%, rgba(180,140,49,0) 72%);
    opacity: 1;
  }
  .section-title {
    position: absolute;
    left: 128px;
    margin: 0;
    font-family: "Arvo", serif;
    font-weight: 700;
    font-size: 40px;
    line-height: 1;
    color: var(--gold);
  }
  .section-title--salad { top: 295px; }
  .section-title--entree { top: 490px; }
  .section-title--cake { top: 813px; }
  .dish-icon {
    position: absolute;
    background: var(--ink);
  }
  .dish-icon--tomato { left: 206px; top: 368px; width: 50px; height: 50px; border-radius: 50%; }
  .dish-icon--cow { left: 190px; top: 545px; width: 70px; height: 55px; border-radius: 8px; }
  .dish-icon--fish { left: 193px; top: 624px; width: 64px; height: 50px; border-radius: 50%; }
  .dish-icon--carrot { left: 199px; top: 702px; width: 54px; height: 66px; border-radius: 40% 40% 50% 10%; }
  .dish-icon--cake { left: 208px; top: 856px; width: 46px; height: 54px; border-radius: 6px 20px 2px 2px; }
  .dish {
    position: absolute;
    left: 291px;
    margin: 0;
    font-family: "Didact Gothic", sans-serif;
    font-size: 24px;
    line-height: 32px;
    color: var(--ink);
  }
  .dish--salad { top: 347px; }
  .dish--beef { top: 545px; }
  .dish--halibut { top: 622px; }
  .dish--agnolotti { top: 702px; }
  .dish--cake { top: 864px; }
</style>
</head>
<body>
<main class="menu-card">
  <svg class="card-disc" width="1200" height="1156" viewBox="0 0 1200 1156" aria-hidden="true">
    <circle cx="600" cy="543" r="594" fill="var(--sand)" stroke="var(--rim)" stroke-width="2"/>
  </svg>

  <div class="ornament ornament--title-left" role="img" aria-label="Small gold scroll ornament"></div>
  <div class="ornament ornament--title-right" role="img" aria-label="Small gold scroll ornament"></div>
  <p class="title-small">THE</p>
  <h1 class="title-large">Menu</h1>

  <h2 class="section-title section-title--salad">Salad</h2>
  <div class="dish-icon dish-icon--tomato" role="img" aria-label="Tomato silhouette icon"></div>
  <p class="dish dish--salad">Grilled Watermelon &amp; Fig Salad: Gem Lettuces,<br>Watermelon, Figs, Toasted Hazelnuts,<br>Balsamic Reduction, Honey-Orange Dressing</p>

  <div class="ornament ornament--divider-one" role="img" aria-label="Small gold scroll divider"></div>

  <h2 class="section-title section-title--entree">Entrée</h2>
  <div class="dish-icon dish-icon--cow" role="img" aria-label="Cow silhouette icon"></div>
  <p class="dish dish--beef">Roasted Filet Mignon, Wild Mushrooms, Garlic Mashed Potatoes,<br>Asparagus with Red Wine Sauce</p>
  <div class="dish-icon dish-icon--fish" role="img" aria-label="Fish silhouette icon"></div>
  <p class="dish dish--halibut">Porcini Crusted Halibut, Lemon-Herb Potatoes, Black Kale,<br>Early Girl Tomatoes</p>
  <div class="dish-icon dish-icon--carrot" role="img" aria-label="Carrot silhouette icon"></div>
  <p class="dish dish--agnolotti">Artichoke Agnolotti, Wild Mushrooms, Baby Arugula,<br>Goat Cheese, White Wine Sauce, Micro herbs</p>

  <div class="ornament ornament--divider-two" role="img" aria-label="Small gold scroll divider"></div>

  <h2 class="section-title section-title--cake">Wedding Cake</h2>
  <div class="dish-icon dish-icon--cake" role="img" aria-label="Cake slice silhouette icon"></div>
  <p class="dish dish--cake">Delicate Butter Pecan With Fresh Raspberry Mouse</p>

  <div class="ornament ornament--flourish" role="img" aria-label="Large gold flourish ornament"></div>
</main>
</body>
</html>
```